Business Card Design

I am a mental health counselor in private practice. I provide counseling to individuals, couples, and adults. There is a design on PrintHaven that I really like. It is 2 talking bubbles joined together by a heart. That is just a suggestion. I'm interested in other ideas. I would like my photo to be on the back of the card, along with the text Danielle Overby Counseling. I would like mint green as my background color and navy writing, if possible. The final design should be elegant, professional, and maybe just a touch whimsical.
Target Market(s)
Individual adolescents, adults, couples, and families seeking counseling.
Industry/Entity Type
Mental Health
Contact Information for Business Card
Danielle Overby
A Wholehearted Approach to Counseling
Danielle Overby, M.S. NCC
Marlowe Lodge
2740 NW Kestrel Avenue, Suite 215
Portland OR 97201
503-862-1157
counselingwithdanielle.example
Requirements
Must have
- The card must have all of the text provided and my photo.
Nice to have
- I like cards that are rounded on the sides, and I like thick paper.

```html
<!DOCTYPE html>
<html lang="en">
<head>
<meta charset="utf-8">
<title>Danielle Overby Counseling – Business Card Back</title>
<link rel="stylesheet" href="https://fonts.googleapis.com/css2?family=Great+Vibes&display=swap">
<style>
  :root {
    --mint: #77fd5b;
    --title-blue: #1b22d2;
    --title-shadow: rgba(10, 20, 60, 0.55);
    --frame-blue: #6b80cc;
    --frame-edge: #9fb0e6;
    --frame-shadow: rgba(20, 40, 20, 0.45);
    --photo-light: #f1efee;
    --photo-mid: #d9d2cc;
    --photo-warm: #e6c79a;
    --photo-dark: #2b2a2c;
  }
  * { margin: 0; padding: 0; box-sizing: border-box; }
  html, body {
    width: 1200px;
    height: 702px;
    overflow: hidden;
    background: var(--mint);
  }
  .card-back {
    position: relative;
    width: 1200px;
    height: 702px;
    background: var(--mint);
  }
  .practice-name {
    position: absolute;
    top: 42px;
    left: 0;
    width: 1200px;
    text-align: center;
    font-family: "Great Vibes", cursive;
    font-weight: 400;
    font-size: 84px;
    line-height: 1;
    color: var(--title-blue);
    text-shadow: 3px 4px 4px var(--title-shadow);
    white-space: nowrap;
  }
  .portrait-frame {
    position: absolute;
    left: 321px;
    top: 175px;
    width: 586px;
    height: 461px;
  }
  .portrait-frame svg {
    position: absolute;
    inset: 0;
    overflow: visible;
  }
  .frame-body {
    fill: var(--frame-blue);
    stroke: var(--frame-edge);
    stroke-width: 3;
  }
  .portrait-photo {
    position: absolute;
    left: 105px;
    top: 102px;
    width: 363px;
    height: 265px;
    background:
      radial-gradient(ellipse 32% 48% at 50% 42%, var(--photo-warm) 0%, rgba(230,199,154,0) 100%),
      linear-gradient(180deg, var(--photo-mid) 0%, var(--photo-light) 42%, var(--photo-light) 70%, var(--photo-dark) 100%);
    box-shadow: inset 0 0 6px rgba(0, 0, 0, 0.35), 0 0 0 2px var(--frame-edge);
  }
</style>
</head>
<body>
  <main class="card-back">
    <h1 class="practice-name">Danielle Overby Counseling</h1>

    <div class="portrait-frame">
      <svg viewBox="0 0 586 461" width="586" height="461" aria-hidden="true">
        <defs>
          <filter id="frame-drop" x="-10%" y="-10%" width="125%" height="125%">
            <feDropShadow dx="5" dy="7" stdDeviation="5" flood-color="var(--frame-shadow)" flood-opacity="0.5"/>
          </filter>
        </defs>
        <path class="frame-body" filter="url(#frame-drop)"
          d="M40 25
             C130 50 200 0 293 0
             C386 0 456 50 546 25
             C550 50 570 65 586 70
             C555 130 600 200 590 230
             C600 260 555 330 586 391
             C570 396 550 410 546 436
             C456 411 386 461 293 461
             C200 461 130 411 40 436
             C36 410 16 396 0 391
             C31 330 -14 260 -4 230
             C-14 200 31 130 0 70
             C16 65 36 50 40 25 Z"/>
      </svg>
      <div class="portrait-photo" role="img"
           aria-label="Portrait photo of Danielle Overby smiling, seated in front of a white bookshelf"></div>
    </div>
  </main>
</body>
</html>
```